Letterhead to Prospective Clients

Create a letterhead (word & canva) that I will use to send letters to prospective clients and also include the Coralwood Estate Partners Logo, My Contact Details and Interchangeable "Suburb". Use the same font and colour pallete

Maris Dulworth | "Suburb" Specialist - Redlands & Surrounds
Mobile: 0417 862 095
Email: MD@CoralwoodEstatePartners.com.au

```html
<!DOCTYPE html>
<html lang="en">
<head>
<meta charset="utf-8">
<title>Coralwood Estate Partners – Letterhead</title>
<link href="https://fonts.googleapis.com/css2?family=Poppins:wght@300;400;600&display=swap" rel="stylesheet">
<style>
  :root {
    --backdrop: #ababab;
    --navy: #001356;
    --gold: #d6a66b;
    --paper: #ffffff;
    --blush: #fdf4f4;
    --white: #ffffff;
  }
  * { margin: 0; padding: 0; box-sizing: border-box; }
  html, body {
    width: 872px;
    height: 1200px;
    overflow: hidden;
    background: var(--backdrop);
    font-family: "Poppins", sans-serif;
  }
  .letterhead {
    position: absolute;
    left: 102px;
    top: 92px;
    width: 678px;
    height: 1017px;
    background: var(--paper);
  }
  .masthead {
    position: absolute;
    left: 0;
    top: 0;
    width: 100%;
    height: 108px;
    background: var(--navy);
  }
  .brand-name {
    position: absolute;
    left: 28px;
    top: 22px;
    width: 116px;
    text-align: center;
    color: var(--gold);
    font-weight: 300;
    font-size: 17px;
    line-height: 20px;
    letter-spacing: 1px;
    text-transform: uppercase;
  }
  .contact-block {
    position: absolute;
    left: 360px;
    top: 14px;
    color: var(--white);
  }
  .agent-name {
    font-weight: 600;
    font-size: 16px;
    line-height: 20px;
  }
  .agent-role {
    font-weight: 400;
    font-size: 13.5px;
    line-height: 18px;
    margin-bottom: 8px;
  }
  .contact-line {
    display: flex;
    align-items: center;
    font-weight: 400;
    font-size: 14px;
    line-height: 16.5px;
  }
  .contact-icon {
    width: 13px;
    height: 13px;
    margin: 0 10px 0 2px;
    flex: none;
  }
  .page-body {
    position: absolute;
    left: 0;
    top: 108px;
    width: 100%;
    height: 896px;
    background: linear-gradient(135deg, var(--paper), var(--blush) 50%, var(--paper));
  }
  .footer-band {
    position: absolute;
    left: 0;
    bottom: 0;
    width: 100%;
    height: 13px;
    background: var(--gold);
  }
</style>
</head>
<body>
  <main class="letterhead">
    <header class="masthead">
      <div class="brand-name">Coralwood<br>Estate</div>
      <div class="contact-block">
        <p class="agent-name">Maris Dulworth</p>
        <p class="agent-role">"Suburb" Specialist Redlands &amp; Surrounds</p>
        <p class="contact-line">
          <svg class="contact-icon" viewBox="0 0 24 24" aria-hidden="true">
            <path fill="var(--gold)" d="M6.6 10.8a15.1 15.1 0 0 0 6.6 6.6l2.2-2.2a1 1 0 0 1 1-.25 11.4 11.4 0 0 0 3.6.57 1 1 0 0 1 1 1V20a1 1 0 0 1-1 1A17 17 0 0 1 3 4a1 1 0 0 1 1-1h3.5a1 1 0 0 1 1 1c0 1.25.2 2.45.57 3.57a1 1 0 0 1-.25 1z"/>
          </svg>
          0417 862 095
        </p>
        <p class="contact-line">
          <svg class="contact-icon" viewBox="0 0 24 24" aria-hidden="true">
            <path fill="var(--gold)" d="M2 5h20v14H2z"/>
            <path fill="none" stroke="var(--navy)" stroke-width="1.6" d="M2 5l10 8 10-8M2 19l7-7M22 19l-7-7"/>
          </svg>
          MD@CoralwoodEstatePartners.com.au
        </p>
      </div>
    </header>
    <section class="page-body" role="img" aria-label="Faint diagonal repeating brand-name pattern in soft blush on white"></section>
    <footer class="footer-band"></footer>
  </main>
</body>
</html>
```